Residential Construction Business - Site Signage

I need a design made for a site fence banner. We have a logo and branding so the design would need to be aligned with this. It would need to be made to specific size ratio so that it can be sent to the maker for production.
ratio : 4600 wide x 1700 high
The design should feature our website and also the slogan
"don't move, re-imagine"

Target Market(s)

potential clients

Industry/Entity Type

construction

Font styles to use
Other font styles liked:
• to match branding

Colors
0054AA
0677BA
7BADD7
CADEEF
E8F1F8

Requirements
Must have
• www.velmbuild.com.au Majority of the sign is our brand logo
Nice to have
• Majority of the sign is our brand logo
Should not have
• colors and themes that arent brand relevant

```html
<!DOCTYPE html>
<html lang="en">
<head>
<meta charset="utf-8">
<title>Velm Build – Site Fence Banner</title>
<link rel="stylesheet" href="https://fonts.googleapis.com/css2?family=Montserrat:wght@600&family=Open+Sans:wght@600;700&display=swap">
<style>
  :root {
    --backdrop: #cccccc;
    --navy-deep: #0b3d5c;
    --navy-mid: #164c70;
    --navy-light: #23597c;
    --white: #ffffff;
  }
  html, body {
    margin: 0;
    padding: 0;
    width: 1200px;
    height: 674px;
    overflow: hidden;
    background: var(--backdrop);
  }
  .canvas {
    position: relative;
    width: 1200px;
    height: 674px;
  }
  .banner {
    position: absolute;
    left: 42px;
    top: 131px;
    width: 1116px;
    height: 412px;
    overflow: hidden;
  }
  .interior-photo {
    position: absolute;
    inset: 0;
    background:
      radial-gradient(ellipse at 78% 30%, var(--navy-light) 0%, transparent 55%),
      linear-gradient(100deg, var(--navy-mid) 0%, var(--navy-deep) 45%, var(--navy-mid) 100%);
  }
  .brand-panel {
    position: absolute;
    left: 49px;
    top: 67px;
    width: 380px;
    height: 278px;
    background: var(--white);
    display: flex;
    flex-direction: column;
    align-items: center;
    justify-content: center;
    color: var(--navy-deep);
    text-align: center;
  }
  .brand-name {
    margin: 0 0 0 0.3em;
    font-family: "Montserrat", sans-serif;
    font-weight: 600;
    font-size: 32px;
    line-height: 1;
    letter-spacing: 0.3em;
    white-space: nowrap;
  }
  .slogan {
    margin: 22px 0 0;
    font-family: "Open Sans", sans-serif;
    font-weight: 700;
    font-size: 18px;
    line-height: 1.2;
  }
  .website {
    margin: 8px 0 0;
    font-family: "Open Sans", sans-serif;
    font-weight: 600;
    font-size: 16px;
    line-height: 1.2;
  }
  .services {
    position: absolute;
    right: 47px;
    top: 43px;
    margin: 0;
    padding: 0;
    list-style: none;
    text-align: right;
    font-family: "Open Sans", sans-serif;
    font-weight: 700;
    font-size: 28px;
    line-height: 29px;
    color: var(--white);
  }
  .services li::after {
    content: "";
    display: inline-block;
    width: 8px;
    height: 8px;
    margin-left: 6px;
    border-radius: 50%;
    background: var(--white);
    vertical-align: middle;
    position: relative;
    top: -2px;
  }
  .contacts {
    position: absolute;
    right: 60px;
    top: 288px;
    display: flex;
    gap: 26px;
    font-family: "Open Sans", sans-serif;
    font-weight: 700;
    font-size: 28px;
    line-height: 31px;
    color: var(--white);
    text-align: right;
  }
  .contact-person { margin: 0; }
  .contact-name, .contact-phone { display: block; white-space: nowrap; }
</style>
</head>
<body>
<main class="canvas">
  <section class="banner">
    <div class="interior-photo" role="img" aria-label="Photo of a finished open-plan living and dining interior, tinted in brand blue"></div>

    <div class="brand-panel">
      <h1 class="brand-name">VELMBUILD</h1>
      <p class="slogan">don't move, re-imagine</p>
      <p class="website">www.velmbuild.com.au</p>
    </div>

    <ul class="services">
      <li>NEW HOMES</li>
      <li>RENOVATIONS</li>
      <li>ADDITIONS</li>
    </ul>

    <div class="contacts">
      <p class="contact-person">
        <span class="contact-name">LIAM HARCOURT</span>
        <span class="contact-phone">0412 580 936</span>
      </p>
      <p class="contact-person">
        <span class="contact-name">NOAH REID</span>
        <span class="contact-phone">0438 217 605</span>
      </p>
    </div>
  </section>
</main>
</body>
</html>
```